Re-design and craft the perfect CV platform

We are building a CV-based platform designed to connect employees and employers, with a strong focus on individual users. As we're just starting out, we're looking to have our platform and logo redesigned to better reflect our vision
https://app.plovanstaffing.com/
Colors like in the logo attached
#87C032 #6A6E71 #618930 - also you can add more colors if you like.
https://app.plovanstaffing.com/dashboard - This page would be nice if you plan it, like personal Bio dashboard. Attached picture (Dashboard wanted) one idea from how we would like to be, but we are open for new professional ideas/solutions.
https://app.plovanstaffing.com/posts - On this page we want to be showed the jobs posted. Attached one picture about our idea (jobs page wanted)
https://app.plovanstaffing.com/profile - design something nice.
Only Photoshop, Illustrator or Figma
Other pictures from the app attached (as looking right now)

Target Market(s)

Job seekers, HR, Recruiters

Industry/Entity Type

HR Tech

Number of Pages Required

5+ page

Colors
00AB8E
00BBA5
67D7C9
C6EFE9
E9F9F6

```html
<!DOCTYPE html>
<html lang="en">
<head>
<meta charset="utf-8">
<title>CVNEXA – Platform Screens</title>
<link href="https://fonts.googleapis.com/css2?family=Poppins:wght@400;500;600;700&display=swap" rel="stylesheet">
<style>
:root{
  --green:#87c032;
  --green-dark:#618930;
  --green-soft:#eef6e3;
  --slate:#6a6e71;
  --ink:#474a4d;
  --muted:#8d9194;
  --line:#e3e3e3;
  --field:#ededed;
  --board:#686b6e;
  --app-bg:#ebebeb;
  --white:#ffffff;
  --btn-dark:#5f6366;
}
*{box-sizing:border-box;margin:0;padding:0}
html,body{width:1200px;height:3114px;overflow:hidden;background:var(--board)}
body{font-family:"Poppins",Arial,sans-serif;color:var(--ink)}
.board{position:relative;width:993px;height:2576px;transform:scale(1.20846);transform-origin:0 0;background:var(--board)}
.board-accent{position:absolute;left:0;top:1500px;width:993px;height:1076px;background:linear-gradient(180deg,rgba(135,192,50,0) 0%,rgba(135,192,50,.35) 45%,rgba(135,192,50,.55) 100%)}
.section-title{position:absolute;left:148px;font-size:26px;font-weight:700;color:var(--white);line-height:1;letter-spacing:-.3px}
.frame{position:absolute;left:148px;width:696px;height:415px;border:5px solid var(--white);border-radius:10px;overflow:hidden;box-shadow:0 8px 24px rgba(0,0,0,.18)}
.abs{position:absolute}

.brand{position:absolute;display:flex;align-items:center;gap:7px}
.brand-dot{width:22px;height:22px;border-radius:50%;background:var(--green)}
.brand-name{font-size:21px;font-weight:600;color:var(--slate);letter-spacing:.3px}
.brand.small{gap:5px}
.brand.small .brand-dot{width:13px;height:13px}
.brand.small .brand-name{font-size:11.5px}

.login-screen{background:linear-gradient(135deg,#ececec 0%,#f3f3f3 60%,#e6e6e6 100%)}
.login-screen.alt{background:linear-gradient(135deg,#f7f8f9 0%,#fbfbfb 55%,#eef0f2 100%)}
.login-card{position:absolute;width:215px;height:219px;background:var(--white);border-radius:14px;box-shadow:0 14px 26px rgba(0,0,0,.09)}
.login-card.outlined{border:1px solid #c8e2a3;box-shadow:0 14px 26px rgba(0,0,0,.06)}
.login-card .card-title{position:absolute;left:18px;top:13px;font-size:10.5px;font-weight:600;color:var(--slate)}
.login-card .card-title em{font-style:normal;color:var(--green)}
.login-card .card-rule{position:absolute;left:18px;right:18px;top:38px;height:1px;background:var(--line)}
.login-card .card-heading{position:absolute;left:18px;top:62px;font-size:8.5px;font-weight:500;color:var(--ink)}
.login-card .card-note{position:absolute;left:18px;top:79px;width:185px;font-size:6px;line-height:9px;color:var(--muted)}
.login-card .field-label{position:absolute;left:18px;top:117px;font-size:5.8px;font-weight:600;color:var(--ink)}
.login-card .field-label b{color:#e05050;font-weight:600}
.pill-input{position:absolute;left:19px;top:131px;width:176px;height:24px;border-radius:12px;background:var(--field);display:flex;align-items:center;padding-left:12px;gap:7px;font-size:5.8px;color:#9a9da0}
.pill-button{position:absolute;left:19px;top:166px;width:176px;height:25px;border-radius:13px;background:var(--green);color:var(--white);font-size:6.3px;font-weight:600;letter-spacing:.3px;display:flex;align-items:center;justify-content:center}
.pill-button .knob{position:absolute;right:4px;top:3.5px;width:18px;height:18px;border-radius:50%;background:var(--white);display:flex;align-items:center;justify-content:center}
.photo-area{position:absolute}

.app-screen{background:var(--app-bg)}
.app-header{position:absolute;left:0;top:0;width:686px;height:51px;background:#ececec;border-bottom:1px solid #e0e0e0}
.app-header .divider{position:absolute;left:84px;top:12px;width:1px;height:28px;background:#d6d6d6}
.app-header .page-title{position:absolute;left:97px;top:19px;font-size:10px;font-weight:600;color:var(--slate);letter-spacing:.1px}
.app-header .page-title em{font-style:normal;color:var(--green)}
.nav-links{position:absolute;left:97px;top:23px}
.nav-links span{position:absolute;font-size:5.6px;font-weight:500;color:var(--slate);white-space:nowrap}
.nav-links .active{color:var(--green)}
.nav-links .active::after{content:"";position:absolute;left:0;right:0;top:10px;height:1px;background:var(--green)}
.chip{position:absolute;top:16px;width:48px;height:17px;border:1px solid #b8babc;border-radius:9px;display:flex;align-items:center;justify-content:center;gap:4px;font-size:6px;color:var(--ink)}
.header-icon{position:absolute;top:19px}

.panel{position:absolute;top:55px;height:333px;background:var(--white);border-radius:7px}

.profile-card{left:18px;width:127px}
.avatar{position:absolute;border-radius:50%;border:1.5px solid #c7d99f;padding:3px;background:var(--white)}
.avatar-fill{width:100%;height:100%;border-radius:50%;background:radial-gradient(circle at 50% 40%,#b9a48f 0%,#8f7b68 45%,#7e8387 100%)}
.profile-card .avatar{left:27px;top:12px;width:74px;height:74px}
.p-name{position:absolute;left:0;right:0;top:96px;text-align:center;font-size:9.5px;font-weight:600;color:var(--ink)}
.p-mail{position:absolute;left:0;right:0;top:109px;text-align:center;font-size:5.6px;color:var(--muted)}
.p-facts{position:absolute;left:15px;top:127px;font-size:5.6px;line-height:11.6px}
.p-facts div{display:flex}
.p-facts b{font-weight:600;width:34px;color:var(--ink)}
.p-facts span{color:var(--muted)}
.p-rule{position:absolute;left:15px;right:15px;height:1px;background:var(--line)}
.p-block{position:absolute;left:15px;font-size:5.6px;line-height:10px}
.p-block b{display:block;font-size:6.2px;font-weight:600;color:var(--ink)}
.p-block span{color:var(--muted)}
.lang{position:absolute;left:15px;width:96px}
.lang .lang-row{display:flex;justify-content:space-between;font-size:5.2px;line-height:7px;color:var(--muted)}
.lang .bar{margin-top:3px;height:3px;border-radius:2px;background:#e6e6e6;overflow:hidden}
.lang .bar i{display:block;height:100%;background:repeating-linear-gradient(90deg,var(--green) 0 2.5px,#a4d15e 2.5px 3.5px)}
.scroll-thumb{position:absolute;width:2px;border-radius:1px;background:#d4d4d4}

.about-card{left:158px;width:371px}
.h-cap{font-size:6.5px;font-weight:600;color:var(--ink);letter-spacing:.1px;line-height:10px}
.txt{font-size:5.6px;color:var(--muted);line-height:8.6px}
.about-card .a-rule{position:absolute;left:16px;right:16px;height:1px;background:var(--line)}
.badge{display:inline-block;margin-left:5px;padding:1.5px 6px;border-radius:6px;background:var(--green);color:var(--white);font-size:4.6px;font-weight:600;line-height:6px;vertical-align:1px}
.bullets{list-style:none}
.bullets li{position:relative;padding-left:8px;font-size:5.6px;line-height:10.3px;color:var(--muted);display:flex}
.bullets li::before{content:"";position:absolute;left:1px;top:3.5px;width:3px;height:3px;border-radius:50%;background:var(--green)}
.bullets li b{font-weight:500;color:var(--ink)}
.bullets.cols li b{width:142px;flex:none}
.bullets.skills li b{width:86px;flex:none}

.jobs-card{left:541px;width:128px}
.tabs{position:absolute;left:12px;top:31px;width:104px;font-size:5.2px;color:var(--ink)}
.tabs span{position:absolute;white-space:nowrap}
.tabs .on{color:var(--green)}
.tabs-rule{position:absolute;left:12px;top:42px;width:104px;height:1px;background:var(--line)}
.tabs-rule i{position:absolute;left:0;top:-.5px;width:22px;height:1.5px;background:var(--green)}
.saved-job{position:absolute;left:14px;width:104px}
.saved-job .logo-dot{position:absolute;left:0;top:0;width:20px;height:20px;border-radius:50%;border:1px solid #e1e1e1;background:var(--white)}
.saved-job .logo-dot i{position:absolute;left:5px;top:5px;width:8px;height:8px;border-radius:50%}
.saved-job .sj-title{position:absolute;left:30px;top:2px;font-size:5.6px;font-weight:600;color:var(--ink);white-space:nowrap}
.saved-job .sj-date{position:absolute;left:30px;top:10px;font-size:4.3px;color:var(--muted);white-space:nowrap}
.saved-job .sj-more{position:absolute;right:0;top:4px}
.saved-job .sj-desc{position:absolute;left:0;top:24px;width:100px;font-size:5px;line-height:7.6px;color:var(--muted)}
.mini-btn{position:absolute;top:47px;height:11px;border-radius:6px;font-size:4.3px;font-weight:600;color:var(--white);display:flex;align-items:center;justify-content:center}
.mini-btn.go{left:0;width:33px;background:var(--green)}
.mini-btn.view{left:37px;width:34px;background:var(--btn-dark)}

.list-card{left:158px;width:511px}
.search{position:absolute;left:17px;top:17px;width:157px;height:19px;border-radius:10px;background:var(--field);font-size:5.4px;color:#9a9da0;display:flex;align-items:center;padding-left:11px}
.search svg{position:absolute;right:9px;top:5.5px}
.tool{position:absolute;top:18px;width:18px;height:18px;border-radius:50%;border:1px solid #d9d9d9;background:var(--white);display:flex;align-items:center;justify-content:center}
.tool.on{background:var(--green);border-color:var(--green)}
.job-row{position:absolute;left:17px;width:476px;height:45px;border-radius:5px;background:#f4f4f4}
.job-row.picked{background:var(--green-soft);border:1px solid #a6d267}
.job-row .co-logo{position:absolute;left:14px;top:10.5px;width:24px;height:24px;border-radius:50%;background:var(--white);border:1px solid #e4e4e4}
.job-row .co-logo i{position:absolute;left:7px;top:7px;width:9px;height:9px;border-radius:50%}
.job-row .co-name{position:absolute;left:48px;top:13px;font-size:5.6px;line-height:8px;color:var(--muted)}
.job-row .co-role{position:absolute;left:48px;top:23px;font-size:6.2px;line-height:9px;font-weight:600;color:var(--ink)}
.job-row .meta{position:absolute;left:193px;top:14px;font-size:4.6px;line-height:10px;color:var(--muted)}
.job-row .meta div{display:flex;align-items:center;gap:3px}
.job-row .pay{position:absolute;left:274px;top:13px}
.job-row .pay b{display:block;font-size:6.6px;line-height:10px;font-weight:600;color:var(--ink)}
.job-row .pay span{display:block;font-size:4.6px;line-height:8px;color:var(--muted)}
.row-btn{position:absolute;top:16px;width:42px;height:13px;border-radius:7px;font-size:4.3px;font-weight:600;color:var(--white);display:flex;align-items:center;justify-content:center}
.row-btn.view{left:375px;background:var(--btn-dark)}
.row-btn.go{left:424px;width:41px;background:var(--green)}

.setup-card{left:18px;width:651px;height:332px;background:var(--white)}
.ghost-btn{position:absolute;left:29px;top:19px;width:54px;height:18px;border:1px solid #c9cbcd;border-radius:9px;font-size:6px;color:var(--ink);display:flex;align-items:center;justify-content:center;gap:4px}
.setup-title{position:absolute;left:0;right:0;top:17px;text-align:center;font-size:17px;line-height:24px;font-weight:600;color:var(--slate)}
.setup-sub{position:absolute;left:0;right:0;top:44px;text-align:center;font-size:7px;color:var(--muted)}
.next-btn{position:absolute;left:554px;top:18px;width:67px;height:20px;border-radius:10px;background:var(--green);color:var(--white);font-size:6.5px;font-weight:600;display:flex;align-items:center;justify-content:center;gap:3px}
.step-line{position:absolute;left:96px;top:90px;width:459px;height:1px;background:#e1e1e1}
.step{position:absolute;top:82px;width:80px;margin-left:-40px;text-align:center}
.step .dot{width:16px;height:16px;margin:0 auto;border-radius:50%;background:#e9e9e9;display:flex;align-items:center;justify-content:center}
.step .dot i{width:9px;height:9px;border-radius:50%;background:var(--btn-dark)}
.step.on .dot{background:var(--green)}
.step .num{margin-top:4px;font-size:5.4px;line-height:7px;color:var(--ink)}
.step .name{font-size:4.7px;line-height:7px;color:var(--muted)}
.step.on .num,.step.on .name{color:var(--green)}
.setup-card .avatar{left:94px;top:167px;width:110px;height:110px;padding:4px}
.upload{position:absolute;left:94px;top:287px;width:120px;display:flex;align-items:center;justify-content:center;gap:4px;font-size:6.6px;font-weight:500;color:var(--ink);text-decoration:underline}
.form-field{position:absolute;width:98px}
.form-field label{display:block;font-size:5.2px;line-height:8px;font-weight:600;color:var(--ink);height:10px}
.form-field label b{color:#e05050;font-weight:600}
.form-field .input{height:20px;border-radius:10px;background:var(--field);font-size:5.4px;color:#9a9da0;display:flex;align-items:center;padding:0 11px;justify-content:space-between}
.save-btn{position:absolute;left:233px;top:290px;width:98px;height:18px;border-radius:9px;background:var(--green);color:var(--white);font-size:6.2px;font-weight:600;display:flex;align-items:center;justify-content:center;gap:4px}
</style>
</head>
<body>
<div class="board">

  <div class="board-accent" role="img" aria-label="Decorative green background accent"></div>

  <h2 class="section-title" style="top:92px">Login Version 1</h2>
  <section class="frame login-screen" style="top:132px">
    <div class="brand" style="left:136px;top:58px"><span class="brand-dot"></span><span class="brand-name">CVNEXA</span></div>
    <div class="login-card" style="left:77px;top:121px">
      <div class="card-title">Recruitment <em>Web App</em> Access</div>
      <div class="card-rule"></div>
      <div class="card-heading">Log in to your account</div>
      <p class="card-note">Welcome to Jordan Vale, please put your login credentials below to start using the app</p>
      <div class="field-label">Email Address<b>*</b></div>
      <div class="pill-input">
        <svg width="8" height="6" viewBox="0 0 8 6"><rect x=".5" y=".5" width="7" height="5" rx="1" fill="#8d9194"/><path d="M.8 1l3.2 2.3L7.2 1" stroke="#ededed" stroke-width=".8" fill="none"/></svg>
        Enter email address
      </div>
      <div class="pill-button">CONTINUE<span class="knob"><svg width="5" height="6" viewBox="0 0 5 6"><path d="M1.5 1l2 2-2 2" stroke="#87c032" stroke-width="1" fill="none"/></svg></span></div>
    </div>
    <div class="photo-area" role="img" aria-label="Photo of a young man in a denim jacket sitting on a green block working on a laptop" style="left:377px;top:33px;width:260px;height:372px;border-radius:120px 120px 0 0;background:linear-gradient(180deg,#d3d5d7 0%,#a9b7c6 40%,#6f8aa8 72%,#87c032 92%,#7cb32d 100%)"></div>
  </section>

  <h2 class="section-title" style="top:596px">Login Version 2</h2>
  <section class="frame login-screen alt" style="top:636px">
    <div class="brand" style="left:118px;top:56px"><span class="brand-dot"></span><span class="brand-name">CVNEXA</span></div>
    <div class="login-card outlined" style="left:60px;top:117px">
      <div class="card-title">Recruitment <em>Web App</em> Access</div>
      <div class="card-rule"></div>
      <div class="card-heading">Log in to your account</div>
      <p class="card-note">Welcome to Jordan Vale, please put your login credentials below to start using the app</p>
      <div class="field-label">Email Address<b>*</b></div>
      <div class="pill-input">
        <svg width="8" height="6" viewBox="0 0 8 6"><rect x=".5" y=".5" width="7" height="5" rx="1" fill="#8d9194"/><path d="M.8 1l3.2 2.3L7.2 1" stroke="#ededed" stroke-width=".8" fill="none"/></svg>
        Enter email address
      </div>
      <div class="pill-button">CONTINUE<span class="knob"><svg width="5" height="6" viewBox="0 0 5 6"><path d="M1.5 1l2 2-2 2" stroke="#87c032" stroke-width="1" fill="none"/></svg></span></div>
    </div>
    <div class="photo-area" role="img" aria-label="Photo of a man in glasses relaxing on a green beanbag with a laptop" style="left:302px;top:74px;width:384px;height:331px;border-radius:160px 0 0 0;background:linear-gradient(160deg,#f1f2f3 0%,#c9ccd0 35%,#8a9096 55%,#93c94a 75%,#87c032 100%)"></div>
  </section>

  <h2 class="section-title" style="top:1092px">Dashboard</h2>
  <section class="frame app-screen" style="top:1132px">
    <header class="app-header">
      <div class="brand small" style="left:17px;top:19px"><span class="brand-dot"></span><span class="brand-name">CVNEXA</span></div>
      <div class="divider"></div>
      <div class="page-title"><em>CVNEXA</em> DASHBOARD</div>
      <div class="chip" style="left:522px"><svg width="6" height="5" viewBox="0 0 6 5"><rect y="1" width="6" height="4" rx=".6" fill="#87c032"/><rect x="2" width="2" height="1.4" fill="none" stroke="#87c032" stroke-width=".6"/></svg>Jobs</div>
      <div class="chip" style="left:576px"><svg width="5" height="6" viewBox="0 0 5 6"><path d="M0 0h3.4L5 1.6V6H0z" fill="#87c032"/></svg>CV</div>
      <svg class="header-icon" style="left:638px" width="10" height="11" viewBox="0 0 10 11"><path d="M5 1a3 3 0 0 1 3 3v3l1 1.5H1L2 7V4a3 3 0 0 1 3-3z" fill="#6a6e71"/><circle cx="5" cy="9.8" r="1" fill="#6a6e71"/><circle cx="8" cy="2" r="1.6" fill="#e05050"/></svg>
      <svg class="header-icon" style="left:661px" width="10" height="11" viewBox="0 0 10 11"><circle cx="4.5" cy="3" r="2.3" fill="#6a6e71"/><path d="M0 10c0-3 2-4.4 4.5-4.4S9 7 9 10z" fill="#6a6e71"/></svg>
    </header>

    <aside class="panel profile-card">
      <div class="avatar"><div class="avatar-fill" role="img" aria-label="Profile photo of Milo Varga"></div></div>
      <div class="p-name">Milo Varga</div>
      <div class="p-mail">hello@milovarga.net</div>
      <div class="p-facts">
        <div><b>Phone:</b><span>+08 555 010 2244</span></div>
        <div><b>Age:</b><span>30</span></div>
        <div><b>Gender:</b><span>Male</span></div>
      </div>
      <div class="p-rule" style="top:165px"></div>
      <div class="p-block" style="top:174px"><b>Field of Expertise (Szakmaja):</b><span>Software Development</span></div>
      <div class="p-rule" style="top:199px"></div>
      <div class="p-block" style="top:207px"><b>Highest Level of Education:</b><span>Master's in Computer Science</span></div>
      <div class="p-rule" style="top:233px"></div>
      <div class="p-block" style="top:248px"><b>Languages:</b></div>
      <div class="lang" style="top:263px"><div class="lang-row"><span>Romanian</span><span>65%</span></div><div class="bar"><i style="width:65%"></i></div></div>
      <div class="lang" style="top:283px"><div class="lang-row"><span>Hungarian</span><span>100%</span></div><div class="bar"><i style="width:100%"></i></div></div>
      <div class="lang" style="top:304px"><div class="lang-row"><span>English</span><span>80%</span></div><div class="bar"><i style="width:80%"></i></div></div>
      <div class="scroll-thumb" style="left:121px;top:226px;height:22px"></div>
    </aside>

    <main class="panel about-card">
      <div class="abs" style="left:16px;top:13px;width:340px">
        <div class="h-cap">ABOUT ME:</div>
        <p class="txt">"Hello! I am Milo, a software developer with over 15 years of experience in full-stack development, specializing in creating robust web and mobile applications. I am passionate about leveraging technology to solve real-world problems and am always eager to learn and adapt to new challenges."</p>
      </div>
      <div class="abs h-cap" style="left:16px;top:62px">YEARS OF WORK EXPERIENCE: <span class="badge">15 YEARS</span></div>
      <div class="a-rule" style="top:84px"></div>
      <div class="abs" style="left:16px;top:93px">
        <div class="h-cap">EDUCATION:</div>
        <ul class="bullets cols">
          <li><b>Bachelor's Degree in Computer Science</b>Danube State University</li>
          <li><b>Master's Degree in Information Technology</b>Central Institute of Technology</li>
        </ul>
      </div>
      <div class="a-rule" style="top:138px"></div>
      <div class="abs" style="left:16px;top:149px">
        <div class="h-cap">QUALIFICATIONS:</div>
        <ul class="bullets">
          <li>Certified Backend Developer</li>
          <li>Cloud Certified Solutions Architect</li>
          <li>UX Design Professional Certificate</li>
        </ul>
      </div>
      <div class="a-rule" style="top:203px"></div>
      <div class="abs" style="left:16px;top:214px">
        <div class="h-cap">SKILLS:</div>
        <ul class="bullets skills">
          <li><b>Programming Languages</b>Typed, Scripting, Functional, Query</li>
          <li><b>Frameworks &amp; Libraries</b>Component UI, Server Runtime, Web MVC</li>
          <li><b>Tools</b>Version Control, Containers, CI/CD, Orchestration</li>
          <li><b>Soft Skills</b>Team Leadership, Project Management, Problem Solving, Communication</li>
          <li><b>Other</b>UX/UI Design, Cloud Computing, Machine Learning Basics</li>
        </ul>
      </div>
      <div class="a-rule" style="top:292px"></div>
      <div class="abs" style="left:20px;top:301px">
        <div class="h-cap">DRIVER'S LICENSE:</div>
        <p class="txt">Yes – Class B (Eligible to drive cars and light vehicles)</p>
      </div>
    </main>

    <aside class="panel jobs-card">
      <div class="abs h-cap" style="left:15px;top:12px">MY JOBS</div>
      <div class="tabs"><span class="on" style="left:0">3 Saved</span><span style="left:34px">12 Applied</span><span style="left:76px">Archived</span></div>
      <div class="tabs-rule"><i></i></div>
      <div class="saved-job" style="top:60px">
        <span class="logo-dot"><i style="background:#3b82c4"></i></span>
        <div class="sj-title">Data Analyst</div>
        <div class="sj-date">Saved on 7 Dec</div>
        <svg class="sj-more" width="2" height="7" viewBox="0 0 2 7"><circle cx="1" cy="1" r=".8" fill="#6a6e71"/><circle cx="1" cy="3.5" r=".8" fill="#6a6e71"/><circle cx="1" cy="6" r=".8" fill="#6a6e71"/></svg>
        <p class="sj-desc">Looking for a seasoned software engineer with a knack for...</p>
        <span class="mini-btn go">APPLY</span><span class="mini-btn view">VIEW JOB</span>
      </div>
      <div class="abs" style="left:12px;top:138px;width:104px;height:1px;background:var(--line)"></div>
      <div class="saved-job" style="top:150px">
        <span class="logo-dot"><i style="background:#d9534f"></i></span>
        <div class="sj-title">Product Manager</div>
        <div class="sj-date">Saved on 7 Dec</div>
        <svg class="sj-more" width="2" height="7" viewBox="0 0 2 7"><circle cx="1" cy="1" r=".8" fill="#6a6e71"/><circle cx="1" cy="3.5" r=".8" fill="#6a6e71"/><circle cx="1" cy="6" r=".8" fill="#6a6e71"/></svg>
        <p class="sj-desc">Seeking a data-driven analyst to interpret complex data sets...</p>
        <span class="mini-btn go">APPLY</span><span class="mini-btn view">VIEW JOB</span>
      </div>
    </aside>
  </section>

  <h2 class="section-title" style="top:1596px">Jobs</h2>
  <section class="frame app-screen" style="top:1636px">
    <header class="app-header">
      <div class="brand small" style="left:17px;top:19px"><span class="brand-dot"></span><span class="brand-name">CVNEXA</span></div>
      <div class="divider"></div>
      <div class="page-title">JOBS</div>
      <div class="chip" style="left:522px"><svg width="6" height="5" viewBox="0 0 6 5"><rect y="1" width="6" height="4" rx=".6" fill="#87c032"/><rect x="2" width="2" height="1.4" fill="none" stroke="#87c032" stroke-width=".6"/></svg>Jobs</div>
      <div class="chip" style="left:576px"><svg width="5" height="6" viewBox="0 0 5 6"><path d="M0 0h3.4L5 1.6V6H0z" fill="#87c032"/></svg>CV</div>
      <svg class="header-icon" style="left:638px" width="10" height="11" viewBox="0 0 10 11"><path d="M5 1a3 3 0 0 1 3 3v3l1 1.5H1L2 7V4a3 3 0 0 1 3-3z" fill="#6a6e71"/><circle cx="5" cy="9.8" r="1" fill="#6a6e71"/><circle cx="8" cy="2" r="1.6" fill="#e05050"/></svg>
      <svg class="header-icon" style="left:661px" width="10" height="11" viewBox="0 0 10 11"><circle cx="4.5" cy="3" r="2.3" fill="#6a6e71"/><path d="M0 10c0-3 2-4.4 4.5-4.4S9 7 9 10z" fill="#6a6e71"/></svg>
    </header>

    <aside class="panel profile-card">
      <div class="avatar"><div class="avatar-fill" role="img" aria-label="Profile photo of Milo Varga"></div></div>
      <div class="p-name">Milo Varga</div>
      <div class="p-mail">hello@milovarga.net</div>
      <div class="p-facts">
        <div><b>Phone:</b><span>+08 555 010 2244</span></div>
        <div><b>Age:</b><span>30</span></div>
        <div><b>Gender:</b><span>Male</span></div>
      </div>
      <div class="p-rule" style="top:165px"></div>
      <div class="p-block" style="top:174px"><b>Field of Expertise (Szakmaja):</b><span>Software Development</span></div>
      <div class="p-rule" style="top:199px"></div>
      <div class="p-block" style="top:207px"><b>Highest Level of Education:</b><span>Master's in Computer Science</span></div>
      <div class="p-rule" style="top:233px"></div>
      <div class="p-block" style="top:248px"><b>Languages:</b></div>
      <div class="lang" style="top:263px"><div class="lang-row"><span>Romanian</span><span>65%</span></div><div class="bar"><i style="width:65%"></i></div></div>
      <div class="lang" style="top:283px"><div class="lang-row"><span>Hungarian</span><span>100%</span></div><div class="bar"><i style="width:100%"></i></div></div>
      <div class="lang" style="top:304px"><div class="lang-row"><span>English</span><span>80%</span></div><div class="bar"><i style="width:80%"></i></div></div>
      <div class="scroll-thumb" style="left:121px;top:226px;height:22px"></div>
    </aside>

    <main class="panel list-card">
      <div class="search">Enter filter keyword
        <svg width="8" height="8" viewBox="0 0 8 8"><circle cx="3.3" cy="3.3" r="2.5" fill="none" stroke="#4a4d50" stroke-width=".9"/><path d="M5.2 5.2L7.5 7.5" stroke="#4a4d50" stroke-width=".9"/></svg>
      </div>
      <span class="tool" style="left:383px"><svg width="7" height="7" viewBox="0 0 7 7"><g fill="none" stroke="#6a6e71" stroke-width=".7"><rect x=".4" y=".4" width="2.6" height="2.6"/><rect x="4" y=".4" width="2.6" height="2.6"/><rect x=".4" y="4" width="2.6" height="2.6"/><rect x="4" y="4" width="2.6" height="2.6"/></g></svg></span>
      <span class="tool on" style="left:406px"><svg width="7" height="6" viewBox="0 0 7 6"><g stroke="#fff" stroke-width=".9"><path d="M0 1h7M0 3h5M0 5h7"/></g></svg></span>
      <span class="tool" style="left:429px"><svg width="7" height="7" viewBox="0 0 7 7"><path d="M.5 .8h6L4.2 3.6v2.8L2.8 5.6V3.6z" fill="none" stroke="#6a6e71" stroke-width=".7"/></svg></span>
      <span class="tool" style="left:452px"><svg width="7" height="7" viewBox="0 0 7 7"><path d="M6 3.5A2.5 2.5 0 1 1 5.2 1.6" fill="none" stroke="#6a6e71" stroke-width=".8"/><path d="M4.6.6l1 1.2-1.4.5" fill="none" stroke="#6a6e71" stroke-width=".8"/></svg></span>
      <span class="tool" style="left:475px"><svg width="2" height="7" viewBox="0 0 2 7"><circle cx="1" cy="1" r=".8" fill="#6a6e71"/><circle cx="1" cy="3.5" r=".8" fill="#6a6e71"/><circle cx="1" cy="6" r=".8" fill="#6a6e71"/></svg></span>

      <article class="job-row" style="top:61px">
        <span class="co-logo"><i style="background:#7b5cd6"></i></span>
        <div class="co-name">Northbeam Labs</div><div class="co-role">Full Stack Developer E-commerce</div>
        <div class="meta"><div><svg width="4" height="5" viewBox="0 0 4 5"><path d="M2 5S0 3 0 2a2 2 0 0 1 4 0c0 1-2 3-2 3z" fill="#5f6366"/></svg>Seattle, USA</div><div><svg width="4" height="4" viewBox="0 0 4 4"><circle cx="2" cy="2" r="2" fill="#5f6366"/><path d="M2 1v1.2h.9" stroke="#fff" stroke-width=".5" fill="none"/></svg>Full-time</div></div>
        <div class="pay"><b>Salary</b><span>€60,000 - €75,000 per year</span></div>
        <span class="row-btn view">VIEW MORE</span><span class="row-btn go">APPLY</span>
      </article>
      <article class="job-row" style="top:110px">
        <span class="co-logo"><i style="background:#a6c940"></i></span>
        <div class="co-name">Ledgerline Capital</div><div class="co-role">Product Manager - FinTech</div>
        <div class="meta"><div><svg width="4" height="5" viewBox="0 0 4 5"><path d="M2 5S0 3 0 2a2 2 0 0 1 4 0c0 1-2 3-2 3z" fill="#5f6366"/></svg>London, UK</div><div><svg width="4" height="4" viewBox="0 0 4 4"><circle cx="2" cy="2" r="2" fill="#5f6366"/><path d="M2 1v1.2h.9" stroke="#fff" stroke-width=".5" fill="none"/></svg>Part-time</div></div>
        <div class="pay"><b>Salary</b><span>£45,000 - £60,000 per year</span></div>
        <span class="row-btn view">VIEW MORE</span><span class="row-btn go">APPLY</span>
      </article>
      <article class="job-row picked" style="top:157px">
        <span class="co-logo"><i style="background:#2f4fa3"></i></span>
        <div class="co-name">Quantora Analytics</div><div class="co-role">Data Engineer Analytics Platform</div>
        <div class="meta"><div><svg width="4" height="5" viewBox="0 0 4 5"><path d="M2 5S0 3 0 2a2 2 0 0 1 4 0c0 1-2 3-2 3z" fill="#5f6366"/></svg>Dublin, Ireland</div><div><svg width="4" height="4" viewBox="0 0 4 4"><circle cx="2" cy="2" r="2" fill="#5f6366"/><path d="M2 1v1.2h.9" stroke="#fff" stroke-width=".5" fill="none"/></svg>Full-time</div></div>
        <div class="pay"><b>Salary</b><span>€55,000 - €70,000 per year</span></div>
        <span class="row-btn view">VIEW MORE</span><span class="row-btn go">APPLY</span>
      </article>
      <article class="job-row" style="top:206px">
        <span class="co-logo"><i style="background:#d93a3a"></i></span>
        <div class="co-name">Lumenfield Tech</div><div class="co-role">UX/UI Designer - SaaS Product</div>
        <div class="meta"><div><svg width="4" height="5" viewBox="0 0 4 5"><path d="M2 5S0 3 0 2a2 2 0 0 1 4 0c0 1-2 3-2 3z" fill="#5f6366"/></svg>Remote</div><div><svg width="4" height="4" viewBox="0 0 4 4"><circle cx="2" cy="2" r="2" fill="#5f6366"/><path d="M2 1v1.2h.9" stroke="#fff" stroke-width=".5" fill="none"/></svg>Full-time</div></div>
        <div class="pay"><b>Salary</b><span>$50 - $70 per hour</span></div>
        <span class="row-btn view">VIEW MORE</span><span class="row-btn go">APPLY</span>
      </article>
      <article class="job-row" style="top:254px">
        <span class="co-logo"><i style="background:#3aa56b"></i></span>
        <div class="co-name">Skyvault Systems</div><div class="co-role">Backend Developer - Cloud</div>
        <div class="meta"><div><svg width="4" height="5" viewBox="0 0 4 5"><path d="M2 5S0 3 0 2a2 2 0 0 1 4 0c0 1-2 3-2 3z" fill="#5f6366"/></svg>Seattle, USA</div><div><svg width="4" height="4" viewBox="0 0 4 4"><circle cx="2" cy="2" r="2" fill="#5f6366"/><path d="M2 1v1.2h.9" stroke="#fff" stroke-width=".5" fill="none"/></svg>Full-time</div></div>
        <div class="pay"><b>Salary</b><span>$80,000 - $100,000 per year</span></div>
        <span class="row-btn view">VIEW MORE</span><span class="row-btn go">APPLY</span>
      </article>
      <div class="scroll-thumb" style="left:505px;top:224px;height:26px"></div>
    </main>
  </section>

  <h2 class="section-title" style="top:2109px">Edit Profile</h2>
  <section class="frame app-screen" style="top:2148px">
    <header class="app-header">
      <div class="brand small" style="left:17px;top:19px"><span class="brand-dot"></span><span class="brand-name">CVNEXA</span></div>
      <div class="divider"></div>
      <nav class="nav-links"><span style="left:0">DASHBOARD</span><span class="active" style="left:57px">PROFILE</span><span style="left:101px">JOB POSTS</span></nav>
      <div class="chip" style="left:522px"><svg width="6" height="5" viewBox="0 0 6 5"><rect y="1" width="6" height="4" rx=".6" fill="#87c032"/><rect x="2" width="2" height="1.4" fill="none" stroke="#87c032" stroke-width=".6"/></svg>Jobs</div>
      <div class="chip" style="left:576px"><svg width="5" height="6" viewBox="0 0 5 6"><path d="M0 0h3.4L5 1.6V6H0z" fill="#87c032"/></svg>CV</div>
      <svg class="header-icon" style="left:638px" width="10" height="11" viewBox="0 0 10 11"><path d="M5 1a3 3 0 0 1 3 3v3l1 1.5H1L2 7V4a3 3 0 0 1 3-3z" fill="#6a6e71"/><circle cx="5" cy="9.8" r="1" fill="#6a6e71"/><circle cx="8" cy="2" r="1.6" fill="#e05050"/></svg>
      <svg class="header-icon" style="left:661px" width="10" height="11" viewBox="0 0 10 11"><circle cx="4.5" cy="3" r="2.3" fill="#6a6e71"/><path d="M0 10c0-3 2-4.4 4.5-4.4S9 7 9 10z" fill="#6a6e71"/></svg>
    </header>

    <main class="panel setup-card">
      <span class="ghost-btn"><svg width="6" height="5" viewBox="0 0 6 5"><path d="M6 2.5H1M2.8.6L.9 2.5l1.9 1.9" stroke="#474a4d" stroke-width=".7" fill="none"/></svg>Back</span>
      <h1 class="setup-title">Set up your profile</h1>
      <p class="setup-sub">Build your CV in six easy steps</p>
      <span class="next-btn">Continue <svg width="6" height="5" viewBox="0 0 6 5"><path d="M0 2.5h5M3.2.6l1.9 1.9-1.9 1.9" stroke="#fff" stroke-width=".7" fill="none"/></svg></span>

      <div class="step-line"></div>
      <div class="step on" style="left:96px"><div class="dot"><svg width="6" height="7" viewBox="0 0 6 7"><path d="M0 0h4l2 2v5H0z" fill="#fff"/></svg></div><div class="num">1</div><div class="name">Personal Details</div></div>
      <div class="step" style="left:172px"><div class="dot"><i></i></div><div class="num">2</div><div class="name">Bio</div></div>
      <div class="step" style="left:249px"><div class="dot"><i></i></div><div class="num">3</div><div class="name">Work Experience</div></div>
      <div class="step" style="left:325px"><div class="dot"><i></i></div><div class="num">4</div><div class="name">Education</div></div>
      <div class="step" style="left:402px"><div class="dot"><i></i></div><div class="num">5</div><div class="name">Skills</div></div>
      <div class="step" style="left:478px"><div class="dot"><i></i></div><div class="num">6</div><div class="name">Preferences</div></div>
      <div class="step" style="left:555px"><div class="dot"><i></i></div><div class="num">7</div><div class="name">Done</div></div>

      <div class="avatar"><div class="avatar-fill" role="img" aria-label="Profile photo of Milo Varga"></div></div>
      <span class="upload"><svg width="7" height="7" viewBox="0 0 7 7"><path d="M3.5 5V.8M1.8 2.4L3.5.7l1.7 1.7M.5 4.5v2h6v-2" stroke="#87c032" stroke-width=".9" fill="none"/></svg>Upload Profile Picture</span>

      <div class="form-field" style="left:233px;top:154px"><label>Name<b>*</b></label><div class="input">Milo Varga</div></div>
      <div class="form-field" style="left:340px;top:154px"><label>Email Address<b>*</b></label><div class="input">hello@milovarga.net</div></div>
      <div class="form-field" style="left:446px;top:154px"><label>Phone Number<b>*</b></label><div class="input">+08 555 010 2244</div></div>
      <div class="form-field" style="left:233px;top:197px"><label>Date of Birth<b>*</b></label><div class="input">1988-12-01<svg width="7" height="7" viewBox="0 0 7 7"><rect x=".4" y="1" width="6.2" height="5.6" rx=".6" fill="none" stroke="#87c032" stroke-width=".7"/><path d="M.4 2.8h6.2" stroke="#87c032" stroke-width=".7"/></svg></div></div>
      <div class="form-field" style="left:340px;top:197px"><label>Address<b>*</b></label><div class="input"></div></div>
      <div class="form-field" style="left:446px;top:197px"><label>City<b>*</b></label><div class="input"></div></div>
      <div class="form-field" style="left:233px;top:240px"><label>State<b>*</b></label><div class="input"></div></div>
      <div class="form-field" style="left:340px;top:240px"><label>Post Code<b>*</b></label><div class="input"></div></div>
      <div class="form-field" style="left:446px;top:240px"><label>Country<b>*</b></label><div class="input"></div></div>

      <span class="save-btn"><svg width="7" height="7" viewBox="0 0 7 7"><path d="M0 0h5.5L7 1.5V7H0z" fill="#fff"/><rect x="1.5" y=".6" width="3" height="1.8" fill="#87c032"/></svg>SAVE</span>
    </main>
  </section>

</div>
</body>
</html>
```